Vela Korth

Graphic design for web pages depicting an environmental solution to human waste streams of plastic, tyres and bio mass, converting waste to energy. Technology used is a pyrolysis plant deconstructing 20tonnes per day of waste. Also touch up of logo

```html
<!DOCTYPE html>
<html lang="en">
<head>
<meta charset="utf-8">
<title>Vela Korth — Waste to Energy</title>
<link href="https://fonts.googleapis.com/css2?family=Poppins:wght@400;500;600&family=Noto+Serif:wght@400;500&display=swap" rel="stylesheet">
<style>
:root{
  --teal:#0b8f90;
  --teal-text:#12898c;
  --green:#6aac3a;
  --green-mid:#2f9a6a;
  --leaf:#5aa845;
  --ink:#3a3a3a;
  --grey:#5b5b5b;
  --white:#ffffff;
  --mist:#c9cec8;
}
*{margin:0;padding:0;box-sizing:border-box}
html,body{width:1200px;height:4203px;overflow:hidden}
body{position:relative;background:var(--white);font-family:'Poppins',sans-serif;color:var(--ink)}
.abs{position:absolute}
.serif{font-family:'Noto Serif',serif}

/* hero */
.hero-art{position:absolute;left:0;top:0}
.brand{position:absolute;left:85px;top:40px;display:flex;align-items:center;gap:10px}
.brand-square{width:26px;height:26px;background:var(--teal)}
.brand-name{font-size:18px;font-weight:600;color:var(--teal)}
.nav{position:absolute;top:64px;right:85px;display:flex;gap:42px;font-size:16px;color:var(--teal-text)}
.nav a{color:inherit;text-decoration:none}
.nav .active{font-weight:600}
.hero-title{position:absolute;top:220px;left:0;width:1200px;text-align:center;font-size:23px;font-weight:600;color:var(--teal-text);line-height:28px}
.btn-light{position:absolute;background:var(--white);color:var(--teal-text);font-weight:600;border-radius:8px;display:flex;align-items:center;justify-content:center}
.join{left:522px;top:296px;width:154px;height:50px;font-size:17px}
.scroll{position:absolute;top:454px;left:0;width:1200px;text-align:center;color:var(--white);font-size:15px;font-weight:500}

/* bands */
.solutions{position:absolute;left:0;top:617px;width:1200px;height:861px;background:linear-gradient(180deg,var(--teal) 0%,var(--green) 100%)}
.projects{position:absolute;left:0;top:2076px;width:1200px;height:514px;background:linear-gradient(180deg,var(--green) 0%,var(--teal) 100%)}
.band-title{position:absolute;left:0;width:1200px;text-align:center;font-family:'Noto Serif',serif;font-weight:500;font-size:26px;color:var(--white)}
.rule{position:absolute;left:188px;width:823px;height:2px;background:rgba(255,255,255,.85)}
.rule.teal{background:var(--teal)}
.solution-label{position:absolute;width:200px;text-align:center;font-size:16px;font-weight:600;color:var(--white)}
.solutions-copy{position:absolute;left:188px;top:1166px;width:475px;font-size:12.6px;line-height:19.6px;text-align:center;color:var(--white)}
.art{position:absolute}

/* who */
.who-title{position:absolute;left:552px;top:1617px;width:460px;text-align:center;font-family:'Noto Serif',serif;font-size:26px;color:var(--grey)}
.who-copy{position:absolute;left:552px;top:1678px;width:460px;text-align:center;font-size:18px;line-height:24px;color:var(--grey)}

/* projects */
.project-photo{position:absolute;top:2231px;width:258px;height:256px}
.project-name{position:absolute;top:2511px;width:258px;text-align:center;color:var(--white);font-size:17px}

/* blog */
.section-title{position:absolute;left:188px;width:823px;text-align:center;font-family:'Noto Serif',serif;font-size:21px;font-weight:500;color:var(--teal-text)}
.post-photo{position:absolute;left:186px;width:147px;height:147px;background:linear-gradient(90deg,#4a3f3c 0%,#a58d80 45%,#d9c7b8 52%,#7a6a66 60%,#3d3637 100%)}
.post{position:absolute;left:350px;width:500px}
.post h3{font-weight:400;font-size:13px;line-height:17px;color:#222}
.post .byline{font-size:8px;color:#777;margin-top:2px}
.post p{font-size:8px;line-height:12.6px;color:#555;margin-top:6px}
.post .more{display:block;font-size:9px;color:var(--leaf);margin-top:34px}
.btn-teal{position:absolute;left:526px;top:3176px;width:147px;height:41px;background:var(--teal);color:var(--white);font-size:14px;display:flex;align-items:center;justify-content:center;border-radius:3px}

/* trust */
.trust-photo{position:absolute;left:0;top:3413px;width:1200px;height:258px;background:linear-gradient(180deg,#7b6d6b 0%,#a9928a 30%,#6b7d8e 55%,#34516b 100%)}
.stat{position:absolute;top:3478px;width:216px;height:128px;background:var(--white);font-family:'Noto Serif',serif;text-align:center;color:#222}
.stat .num{position:absolute;top:24px;width:100%;font-size:19px}
.stat .bar{position:absolute;top:68px;left:43px;width:130px;height:1.5px;background:var(--leaf)}
.stat .label{position:absolute;top:84px;width:100%;font-size:16px}

/* closing */
.closing-copy{position:absolute;left:262px;top:3940px;width:375px;text-align:center;color:var(--white);font-size:16px;line-height:18.4px;font-weight:500}
.contact{left:501px;top:4065px;width:129px;height:39px;font-size:15px}
.footer-rule{position:absolute;left:85px;top:4143px;width:1030px;height:1px;background:rgba(255,255,255,.6)}
.footer-brand{position:absolute;left:85px;top:4158px;display:flex;align-items:center;gap:6px;color:var(--white);font-size:11px;font-weight:600}
.footer-brand span.sq{width:12px;height:12px;background:var(--white)}
.copyright{position:absolute;right:85px;top:4167px;color:var(--white);font-size:7px;font-weight:600}
</style>
</head>
<body>

<!-- hero -->
<svg class="hero-art" width="1200" height="540" role="img" aria-label="Photograph of a misty forested mountain valley">
  <defs>
    <linearGradient id="heroMist" x1="0" y1="0" x2="0" y2="1">
      <stop offset="0" stop-color="#d9dcd6"/>
      <stop offset="0.45" stop-color="#c5cbc3"/>
      <stop offset="0.75" stop-color="#7f9079"/>
      <stop offset="1" stop-color="#3f5a3e"/>
    </linearGradient>
  </defs>
  <path d="M0 0H1200V300C1080 610 120 610 0 300Z" fill="url(#heroMist)"/>
</svg>
<div class="brand"><span class="brand-square"></span><span class="brand-name">Vela Korth</span></div>
<nav class="nav">
  <a class="active">Home</a><a>Solutions</a><a>About Us</a><a>Projects</a><a>Blog</a><a>Contact</a>
</nav>
<h1 class="hero-title">Stop wasting our planet's time...<br>Let's start recycling our wastes</h1>
<div class="btn-light join">Join Us</div>
<div class="scroll">Scroll Down</div>
<svg class="abs" style="left:575px;top:484px" width="50" height="26"><path d="M2 3L25 23L48 3" fill="none" stroke="#fff" stroke-width="3"/></svg>

<!-- solutions -->
<section class="solutions"></section>
<h2 class="band-title" style="top:648px">Our Solutions</h2>
<div class="rule" style="top:717px"></div>
<svg class="abs" style="left:0;top:820px" width="1200" height="150" fill="none" stroke="#fff" stroke-width="6" stroke-linecap="round" stroke-linejoin="round">
  <g transform="translate(239,73)">
    <ellipse rx="46" ry="64"/><ellipse rx="30" ry="48"/><ellipse rx="14" ry="26"/>
  </g>
  <path d="M334 73H368M351 56V90"/>
  <g transform="translate(478,73)">
    <path d="M-60 -10A60 60 0 0 1 10 -59"/><path d="M60 10A60 60 0 0 1 -10 59"/>
    <path d="M0 -68L12 -58L0 -48"/><path d="M0 68L-12 58L0 48"/>
    <rect x="-14" y="-28" width="28" height="64" rx="8"/><path d="M-7 -28V-40H7V-28M-14 -4H14M-14 14H14"/>
  </g>
  <path d="M586 73H620M603 56V90"/>
  <g transform="translate(719,78)">
    <path d="M0 -40C-20 -54 -54 -48 -54 -8C-54 32 -30 58 -14 58C-6 58 -4 54 0 54C4 54 6 58 14 58C30 58 54 32 54 -8C54 -48 20 -54 0 -40Z"/>
    <path d="M0 -40C0 -54 6 -66 18 -74M6 -60C18 -72 32 -70 36 -64C24 -56 14 -56 6 -60Z"/>
  </g>
  <path d="M816 64H850M816 82H850"/>
  <path d="M920 10H1006L968 58H1004L942 138L960 80H920Z"/>
</svg>
<div class="solution-label" style="left:139px;top:994px">Tires Recycling</div>
<div class="solution-label" style="left:378px;top:994px">Plastic Recycling</div>
<div class="solution-label" style="left:619px;top:994px">Compost Recycling</div>
<div class="solution-label" style="left:850px;top:994px">Energy</div>
<div class="rule" style="top:1077px"></div>
<p class="solutions-copy">Lorem ipsum dolor sit amet, consectetur adipisicing elit, sed do eiusmod tempor incididunt ut labore et dolore magna aliqua. Ut enim ad minim veniam, quis nostrud exercitation ullamco laboris nisi ut aliquip ex ea commodo consequat. Duis aute irure dolor in reprehenderit in voluptate velit esse cillum dolore eu fugiat nulla pariatur. Excepteur sint occaecat cupidatat non proident, sunt in culpa qui officia deserunt mollit anim id est laborum. Sed ut perspiciatis unde omnis iste natus error sit voluptatem accusantium doloremque laudantium, totam rem aperiam, eaque ipsa quae ab illo inventore veritatis et quasi architecto</p>
<svg class="art" style="left:718px;top:1123px" width="294" height="268" role="img" aria-label="Illustration of a person sorting waste into two recycling bins">
  <path d="M40 60C70 0 190 -10 230 40C270 90 300 130 280 200C260 260 160 268 80 260C10 252 -10 200 10 150C20 120 20 100 40 60Z" fill="#8dc07a" opacity="0.7"/>
</svg>

<!-- who are we -->
<svg class="art" style="left:188px;top:1613px" width="282" height="265" role="img" aria-label="Illustration of a hand holding a globe with growing trees">
  <path d="M60 30C120 -10 180 10 210 60C240 110 300 150 270 220C240 270 140 270 80 250C20 230 -10 180 10 120C20 80 30 50 60 30Z" fill="#e3efdc"/>
</svg>
<h2 class="who-title">Who Are We</h2>
<p class="who-copy">Lorem ipsum dolor sit amet, consectetur adipisicing elit, sed do eiusmod tempor incididunt ut labore et dolore magna aliqua. Ut enim ad minim veniam, quis nostrud exercitation ullamco laboris nisi ut aliquip ex ea commodo consequat. Duis aute irure dolor in reprehenderit in voluptate velit esse cillum dolore eu fugiat nulla pariatur. Excepteur sint occaecat cupidatat non proident, sunt in culpa qui of-f</p>

<!-- projects -->
<section class="projects"></section>
<h2 class="band-title" style="top:2106px">Related Projects</h2>
<div class="rule" style="top:2158px"></div>
<div class="project-photo" style="left:188px;background:linear-gradient(180deg,#3f7fc2 0%,#9cc3e6 55%,#3b4a66 85%,#7d7f72 100%)" role="img" aria-label="Photograph of solar panels under a blue sky"></div>
<div class="project-photo" style="left:470px;background:linear-gradient(180deg,#8a6a86 0%,#e08b5c 40%,#c66a3a 60%,#6e4b2a 100%)" role="img" aria-label="Photograph of wind turbines over a field at sunset"></div>
<div class="project-photo" style="left:753px;background:linear-gradient(180deg,#6e6f80 0%,#b07a5a 50%,#d9833a 75%,#5a3c2a 100%)" role="img" aria-label="Photograph of power line pylons at dusk"></div>
<div class="project-name" style="left:188px">Solar Energy</div>
<div class="project-name" style="left:470px">Eco Energy</div>
<div class="project-name" style="left:753px">Hydraulic Energy</div>

<!-- blog -->
<h2 class="section-title" style="top:2715px">From The Blog</h2>
<div class="rule teal" style="top:2751px"></div>
<div class="post-photo" style="top:2814px" role="img" aria-label="Photograph of a city street between tall buildings"></div>
<article class="post" style="top:2817px">
  <h3>Lorem ipsum dolor sit amet, consectetur Lorem ipsum dolor sit<br>sed do eiusmod tempor incididunt ut.</h3>
  <div class="byline">By Rowan / Blog</div>
  <p>Lorem ipsum dolor sit amet, consectetur adipisicing elit, sed do eiusmod tempor incididunt ut labore et dolore magna aliqua. Ut enim ad minim veniam, quis nostrud exercitation ullamco laboris nisi ut aliquip ex ea commodo consequat. Duis aute irure dolor in reprehenderit in voluptate velit esse cillum dolore eu fugiat.</p>
  <span class="more">Read More »</span>
</article>
<div class="post-photo" style="top:2987px" role="img" aria-label="Photograph of a city street between tall buildings"></div>
<article class="post" style="top:2990px">
  <h3>Lorem ipsum dolor sit amet, consectetur Lorem ipsum dolor sit<br>sed do eiusmod tempor incididunt ut.</h3>
  <div class="byline">By Rowan / Blog</div>
  <p>Lorem ipsum dolor sit amet, consectetur adipisicing elit, sed do eiusmod tempor incididunt ut labore et dolore magna aliqua. Ut enim ad minim veniam, quis nostrud exercitation ullamco laboris nisi ut aliquip ex ea commodo consequat. Duis aute irure dolor in reprehenderit in voluptate velit esse cillum dolore eu fugiat.</p>
  <span class="more">Read More »</span>
</article>
<svg class="art" style="left:890px;top:2820px" width="302" height="253" role="img" aria-label="Illustration of a gardener tending a large plant">
  <path d="M10 170C20 110 60 90 90 50C120 10 170 0 200 40C230 80 260 100 290 120C310 150 290 190 250 200C180 215 80 215 30 205C10 200 5 190 10 170Z" fill="#d4e7cb"/>
  <ellipse cx="150" cy="228" rx="130" ry="12" fill="#3d8a2e"/>
</svg>
<div class="btn-teal">Browse Our Blog</div>

<!-- trust -->
<h2 class="section-title" style="top:3341px">Trust Our Process</h2>
<div class="rule teal" style="top:3374px"></div>
<div class="trust-photo" role="img" aria-label="Photograph of colourful waterfront houses across the water"></div>
<div class="stat" style="left:85px"><div class="num">5+</div><div class="bar"></div><div class="label">Years Of Experience</div></div>
<div class="stat" style="left:358px"><div class="num">300+</div><div class="bar"></div><div class="label">Planted Trees</div></div>
<div class="stat" style="left:625px"><div class="num">200K+</div><div class="bar"></div><div class="label">Tonnes Recycled</div></div>
<div class="stat" style="left:898px"><div class="num">10000+ W</div><div class="bar"></div><div class="label">Energy Produced</div></div>

<!-- closing -->
<svg class="abs" style="left:0;top:0" width="1200" height="4203">
  <defs>
    <linearGradient id="closingFill" x1="0" y1="0" x2="0" y2="1">
      <stop offset="0" stop-color="#0b9190"/>
      <stop offset="1" stop-color="#3aa057"/>
    </linearGradient>
  </defs>
  <path d="M0 3985C200 3765 1000 3765 1200 3985V4203H0Z" fill="url(#closingFill)"/>
</svg>
<p class="closing-copy">Lorem ipsum dolor sit amet, consectetur adipisicing elit, sed do eiusmod tempor incididunt ut labore et dolore magna aliqua. Ut enim ad minim veniam, quis nostrud exercitation ullamco laboris nisi ut aliquip ex ea commodo consequat. Duis aute irure</p>
<div class="btn-light contact">Contact Us</div>
<svg class="art" style="left:764px;top:3919px" width="203" height="176" role="img" aria-label="Illustration of a globe with a factory emitting smoke">
  <path d="M40 40C80 0 150 10 170 50C195 90 210 130 180 160C150 185 80 180 40 160C5 140 -5 90 40 40Z" fill="#e6f1e0" opacity="0.9"/>
</svg>
<div class="footer-rule"></div>
<div class="footer-brand"><span class="sq"></span>Vela Korth</div>
<div class="copyright">Vela Korth 2020. All Rights Reserved</div>

</body>
</html>
```